Industry automation wholesale website

www.velqora.eu provides solutions for automation, building automation and digital signage.

Our products are rugged, reliable, energy saving and representative.

Scope of pages:
● welcome page
- scope of products
- applications, success stories and news
● category page
- short introduction
- sub categories
- product highlights
● product page
- short introduction
- about 3 to 4 pictures
- technical specifications: materials, dimensions
- price
- related products

Optional:
● contact page
- address
- contact form
● blog
- picture
- text
● logo
● favicon / apple touch icon

Conclusion:
● We need a professionally looking site
● Bright colors (e.g. white, grey, metalic colors, blue)

some pages we like:
http://www.brundafel.de/
http://www.korvimash.de/

Target Market(s)

Our target market is the industrial sector
● Target audience: engineering and IT professionals

Industry/Entity Type

Building

Requirements
Must have
• ● only use free available fonts e.g. Pellor Type Library (http://www.pellortype.com/webfonts)
Should not have
• ● sound
● flash

```html
<!DOCTYPE html>
<html lang="en">
<head>
<meta charset="utf-8">
<title>Velqora – Industrial Automation</title>
<link href="https://fonts.googleapis.com/css2?family=Open+Sans:wght@400;600;700&family=Arimo:wght@400;700&display=swap" rel="stylesheet">
<style>
:root{
  --blue:#1f6f9c;
  --blue-dark:#17587d;
  --blue-light:#2b8fc0;
  --nav-top:#3e9ccb;
  --nav-bottom:#1e76a4;
  --hero-a:#6fc0e2;
  --hero-b:#b9e4f3;
  --text:#333;
  --muted:#777;
  --line:#e2e2e2;
  --panel:#f2f2f2;
  --btn:#26323a;
  --footer:#3b5260;
  --footer-line:#566b78;
  --bottom:#262b2f;
}
*{box-sizing:border-box;margin:0;padding:0}
html,body{width:854px;height:1200px;overflow:hidden;background:#fff}
body{font-family:Arimo,Arial,sans-serif;color:var(--text);font-size:8px}
.page{position:relative;width:854px;height:1200px;overflow:hidden}
.abs{position:absolute}
a{color:inherit}

/* header */
.brand{left:114px;top:24px;font-family:"Open Sans",Arial,sans-serif;font-size:40px;font-weight:600;color:var(--blue);letter-spacing:-1px;display:flex;align-items:center;gap:8px}
.brand .dot{width:12px;height:12px;background:var(--blue);display:inline-block}
.topbar{top:11px;font-size:8px;color:#444;display:flex;align-items:center;gap:4px}
.topbar svg{width:9px;height:9px}
.lang-label{left:624px;top:12px;font-size:8.5px;color:var(--blue)}
.lang-select{left:670px;top:10px;width:70px;height:14px;border:1px solid #ccc;font-size:7px;padding:2px 3px;color:#555}
.lang-select b{position:absolute;right:1px;top:1px;width:10px;height:10px;background:#ddd;border:1px solid #999}
.lang-select b:after{content:"";position:absolute;left:2px;top:3px;border:3px solid transparent;border-top-color:#333}
.search{left:359px;top:50px;width:195px;height:20px;border:1px solid #ccc;font-size:7.5px;color:#999;padding:5px 5px}
.search-btn{left:534px;top:50px;width:20px;height:20px;background:var(--blue-light);display:flex;align-items:center;justify-content:center}
.adv{left:499px;top:75px;font-size:7.5px;text-decoration:underline;color:#333}
.cart{left:606px;top:50px;width:134px;height:20px;border:1px solid #ddd;font-size:8px;display:flex;align-items:center;gap:5px;padding-left:8px}
.cart span{color:var(--blue-light)}

/* nav */
.nav{top:104px;left:0;width:854px;height:24px;background:linear-gradient(var(--nav-top),var(--nav-bottom));border-bottom:2px solid #8cc8e2}
.nav ul{list-style:none;position:absolute;left:114px;top:0;display:flex;height:22px}
.nav li{color:#fff;font-family:"Open Sans",Arial,sans-serif;font-size:8.5px;text-transform:uppercase;display:flex;align-items:center;justify-content:center;border-right:1px solid rgba(255,255,255,.18)}
.nav li.active{background:#243039}

/* hero */
.hero{top:128px;left:0;width:854px;height:221px;background:linear-gradient(90deg,var(--hero-a) 0%,var(--hero-b) 35%,var(--hero-a) 70%,#8fd0ea 100%)}
.hero-visual{left:116px;top:28px;width:192px;height:160px;border-radius:4px;background:linear-gradient(135deg,#55595c 0%,#3a3d40 30%,#2c9cc9 55%,#7ed0ee 80%,#4a4e52 100%)}
.hero-title{left:406px;top:58px;font-family:"Open Sans",Arial,sans-serif;font-weight:700;font-size:16.5px;color:var(--blue);text-shadow:0 0 3px #fff}
.hero-rule{left:408px;width:261px;height:3px;border-top:1px solid #fff;border-bottom:1px solid #fff;opacity:.85}
.hero-list{left:410px;top:98px;list-style:none;font-size:10px;color:#222;line-height:19px}
.hero-list li{display:flex;align-items:center;gap:6px}
.hero-list u{color:#173e56}

/* sidebar */
.side-head{left:114px;width:175px;height:21px;background:linear-gradient(90deg,var(--blue) 75%,#3d8cb8);color:#fff;font-family:"Open Sans",Arial,sans-serif;font-size:12.5px;padding:2px 12px}
.cats{left:114px;top:394px;width:175px;border:1px solid var(--line);list-style:none}
.cats li{height:22px;border-bottom:1px solid var(--line);font-family:"Open Sans",Arial,sans-serif;font-size:8px;color:#555;display:flex;align-items:center;justify-content:space-between;padding:0 14px}
.cats li:last-child{border-bottom:0}
.cats li.current{background:var(--panel);color:#111}
.news{left:114px;top:638px;width:175px;height:218px;border:1px solid var(--line);border-top:0}
.news-item{position:absolute;left:0;width:173px;height:86px;border-bottom:1px solid var(--line)}
.news-num{position:absolute;left:14px;top:13px;width:26px;height:26px;background:var(--blue);color:#fff;font-family:"Open Sans",Arial,sans-serif;font-size:13px;display:flex;align-items:center;justify-content:center}
.news-title{position:absolute;left:53px;top:12px;width:110px;font-weight:700;font-size:8px;color:#333;line-height:10px}
.news-text{position:absolute;left:53px;top:37px;width:110px;font-size:7.8px;color:var(--muted);line-height:9.7px}
.btn{background:var(--btn);color:#fff;font-size:8px;display:flex;align-items:center;justify-content:center;border-radius:1px}
.newsletter{left:114px;top:872px;width:175px;height:114px;background:var(--panel)}
.newsletter h3{position:absolute;left:13px;top:8px;font-family:"Open Sans",Arial,sans-serif;font-weight:400;font-size:14px;color:var(--blue)}
.field{position:absolute;left:13px;width:146px;height:18px;border:1px solid #ccc;background:#fff;font-size:7.5px;color:#999;padding:4px 5px}

/* welcome */
.welcome h2{left:328px;top:372px;font-size:16.5px;color:var(--blue);font-family:"Open Sans",Arial,sans-serif;font-weight:400}
.welcome p{left:328px;top:401px;width:222px;font-size:8px;line-height:10px;color:#444}
.more{left:328px;top:449px;font-size:8px;font-weight:700;color:var(--blue)}
.vdiv{left:578px;top:370px;width:1px;height:92px;background:var(--line)}
.solutions h3{left:610px;top:373px;font-family:"Open Sans",Arial,sans-serif;font-weight:400;font-size:13px;color:var(--blue)}
.solutions ul{left:612px;top:398px;list-style:none;font-size:8px;color:#444;line-height:19px;text-transform:uppercase}
.solutions li{display:flex;align-items:center;gap:6px}

/* products */
.products{left:328px;top:484px;width:412px;height:502px;border:1px solid var(--line)}
.products-head{position:absolute;left:0;top:0;width:410px;height:40px;background:var(--panel);border-bottom:1px solid var(--line)}
.products-head h2{position:absolute;left:18px;top:11px;font-family:"Open Sans",Arial,sans-serif;font-weight:400;font-size:13px;color:var(--blue)}
.products-head .btn{position:absolute;left:305px;top:10px;width:94px;height:19px;font-size:7.8px}
.product{position:absolute;left:0;width:410px}
.product h3{position:absolute;left:18px;top:0;font-family:"Open Sans",Arial,sans-serif;font-weight:400;font-size:8.6px;color:#222;text-transform:uppercase}
.product p{position:absolute;left:19px;width:232px;font-size:8.2px;line-height:9.8px;color:var(--muted)}
.product .btn{position:absolute;left:18px;width:65px;height:19px}
.product .photo{position:absolute;left:274px;width:125px;border:1px solid #cfe1ea}
.sep{position:absolute;left:0;width:410px;height:6px;background:linear-gradient(#ececec,#fff)}

/* footer */
.footer{left:0;top:1010px;width:854px;height:168px;background:var(--footer);color:#fff}
.footer h3{position:absolute;top:15px;font-family:"Open Sans",Arial,sans-serif;font-weight:400;font-size:13px;color:#b9dcec}
.fdiv{position:absolute;top:22px;width:1px;height:132px;background:var(--footer-line)}
.fcontact{position:absolute;left:114px;top:44px;font-size:8px;line-height:10px}
.quick{position:absolute;left:312px;top:44px;list-style:none;font-size:8px;line-height:15px}
.social{position:absolute;left:452px;top:40px;display:flex;gap:6px}
.social span{width:18px;height:18px;border-radius:50%;background:#6d8594}
.social span:first-child{background:#3f6fb0}
.testi{position:absolute;left:598px;top:46px;width:132px;font-size:8px;line-height:10px}
.readmore{position:absolute;left:598px;top:127px;width:60px;height:17px;background:var(--blue-light);font-size:7.5px;font-weight:700;display:flex;align-items:center;justify-content:center}
.bottom{left:0;top:1178px;width:854px;height:22px;background:var(--bottom);color:#fff;font-size:7.5px}
</style>
</head>
<body>
<div class="page">

  <div class="abs brand"><span>velqora</span><span class="dot"></span></div>

  <div class="abs topbar" style="left:414px">
    <svg viewBox="0 0 10 10"><path d="M2 0.5 L3.6 2.8 L2.8 4 Q4 6.2 6 7.2 L7.2 6.4 L9.5 8 L8.4 9.6 Q3.5 9 0.4 1.6 Z" fill="#222"/></svg>
    +49 211 5550192
  </div>
  <div class="abs topbar" style="left:512px">
    <svg viewBox="0 0 10 10"><rect x="0.5" y="2" width="9" height="6" fill="#222"/><path d="M0.5 2 L5 5.5 L9.5 2" stroke="#fff" stroke-width=".8" fill="none"/></svg>
    <u>info@velqora.de</u>
  </div>
  <div class="abs lang-label">Language</div>
  <div class="abs lang-select">English<b></b></div>

  <div class="abs search">Product Search ...</div>
  <div class="abs search-btn">
    <svg width="12" height="12" viewBox="0 0 12 12"><circle cx="5" cy="5" r="3.4" stroke="#fff" stroke-width="1.6" fill="none"/><path d="M7.5 7.5 L11 11" stroke="#fff" stroke-width="2"/></svg>
  </div>
  <div class="abs adv">Advance Search</div>
  <div class="abs cart">
    <svg width="14" height="12" viewBox="0 0 14 12"><path d="M0 1 H2.5 L4.5 8 H11.5 L13 3 H3.5" stroke="#222" stroke-width="1.3" fill="none"/><circle cx="5.5" cy="10.5" r="1.2" fill="#222"/><circle cx="10.5" cy="10.5" r="1.2" fill="#222"/></svg>
    Shopping Cart : <span>0 Item (s)</span>
  </div>

  <nav class="abs nav">
    <ul>
      <li class="active" style="width:76px">Home</li>
      <li style="width:92px">Solutions</li>
      <li style="width:88px">Products</li>
      <li style="width:101px">New &amp; Events</li>
      <li style="width:75px">Career</li>
      <li style="width:94px;border-right:0">Contact Us</li>
    </ul>
  </nav>

  <section class="abs hero">
    <div class="abs hero-visual" role="img" aria-label="Touch panel PC with a colourful flower photo on its screen"></div>
    <h1 class="abs hero-title">Touch Panel PC / Bedienterminal</h1>
    <div class="abs hero-rule" style="top:89px"></div>
    <ul class="abs hero-list">
      <li><svg width="10" height="9" viewBox="0 0 10 9"><path d="M1 4.5 L4 7.5 L9 1.5" stroke="#1f6f9c" stroke-width="2" fill="none"/></svg><u>Induatrial</u> :&nbsp; IP65 Front, 24/7 Continuous Operation</li>
      <li><svg width="10" height="9" viewBox="0 0 10 9"><path d="M1 4.5 L4 7.5 L9 1.5" stroke="#1f6f9c" stroke-width="2" fill="none"/></svg><u>Performance</u> :&nbsp; Corvex Dual Core V410 1,6&nbsp; GHz</li>
      <li><svg width="10" height="9" viewBox="0 0 10 9"><path d="M1 4.5 L4 7.5 L9 1.5" stroke="#1f6f9c" stroke-width="2" fill="none"/></svg><u>Fanless</u> :&nbsp; Low Heat Emission, Power Savins</li>
    </ul>
    <div class="abs hero-rule" style="top:159px"></div>
  </section>

  <div class="abs side-head" style="top:370px">Range of Products</div>
  <ul class="abs cats">
    <li class="current">RS422 / RS485 Converter <span>»</span></li>
    <li>RS422 / RS485 Repeater <span>»</span></li>
    <li>RS485 Remote IO <span>»</span></li>
    <li>RS485 Modbus IO <span>»</span></li>
    <li>Embedded Systems <span>»</span></li>
    <li>PCI-Series <span>»</span></li>
    <li>Industry PC <span>»</span></li>
    <li>Industrial Display <span>»</span></li>
    <li>Din Rail Power Supply <span>»</span></li>
  </ul>

  <div class="abs side-head" style="top:616px">Latest News</div>
  <div class="abs news">
    <div class="news-item" style="top:0">
      <div class="news-num">01</div>
      <div class="news-title">Lorem Ipsum is simply dummy text</div>
      <div class="news-text">Lorem ipsum dolor sit amet, consectetur adipisicing elit, sed do eiusmod tempor incididunt ut ...</div>
    </div>
    <div class="news-item" style="top:86px">
      <div class="news-num">02</div>
      <div class="news-title">Lorem Ipsum is simply dummy text</div>
      <div class="news-text">Lorem ipsum dolor sit amet, consectetur adipisicing elit, sed do eiusmod tempor incididunt ut ...</div>
    </div>
    <div class="abs btn" style="left:14px;top:186px;width:60px;height:19px">Read More</div>
  </div>

  <div class="abs newsletter">
    <h3>Newsletter</h3>
    <div class="field" style="top:34px">Name ...</div>
    <div class="field" style="top:58px">Email ...</div>
    <div class="abs btn" style="left:15px;top:84px;width:45px;height:19px">Signup</div>
  </div>

  <div class="welcome">
    <h2 class="abs">Welcome to Our Site</h2>
    <p class="abs">Lorem ipsum dolor sit amet, consectetur adipisicing elit, sed do eiusmod tempor incididunt ut labore et dolore magna aliqua. Ut enim ad minim veniam, quis nostrud exercitation ullamco laboris.</p>
    <div class="abs more">more ...</div>
  </div>
  <div class="abs vdiv"></div>
  <div class="solutions">
    <h3 class="abs">Our Solutions</h3>
    <ul class="abs">
      <li><svg width="9" height="8" viewBox="0 0 10 9"><path d="M1 4.5 L4 7.5 L9 1.5" stroke="#888" stroke-width="2" fill="none"/></svg>Automation</li>
      <li><svg width="9" height="8" viewBox="0 0 10 9"><path d="M1 4.5 L4 7.5 L9 1.5" stroke="#888" stroke-width="2" fill="none"/></svg>Building Automation</li>
      <li><svg width="9" height="8" viewBox="0 0 10 9"><path d="M1 4.5 L4 7.5 L9 1.5" stroke="#888" stroke-width="2" fill="none"/></svg>Digital Signage</li>
    </ul>
  </div>

  <section class="abs products">
    <div class="products-head">
      <h2>Most Popula Products</h2>
      <div class="btn">View All Our Products</div>
    </div>

    <div class="product" style="top:62px">
      <h3>Modbus RTU / RS485 Remote IO Modules</h3>
      <p style="top:15px">RS485 Remote IO modules are ideal to realize decentralized distributed IO units over long distances. We provide the whole product range form Remote IO Modules with RS485 Bus and Modbus RTU such as analogue IO Modules, digital IO Modules, Relay Modules and Timer / Counter Modules. Also we provide RS422 and RS485 converter to RS232,</p>
      <div class="btn" style="top:88px">View Details</div>
      <div class="photo" style="top:-7px;height:94px;background:linear-gradient(135deg,#d7ecf6 0%,#4ea6d4 40%,#3b7fb0 70%,#6fb7d8 100%)" role="img" aria-label="Row of blue remote IO modules on a DIN rail"></div>
    </div>
    <div class="sep" style="top:183px"></div>

    <div class="product" style="top:202px">
      <h3>Touch Panel Industry Computer</h3>
      <p style="top:18px">Velqora provide prestigious Touch Panel Computer for your building automation. Also we provide Human Machine Interfaces for e.g. shopping malls, hotels or hospitals. VantaDAQ Industry Computer are also used e.g. as POS-terminal, for home automation or surveillance systems. Building automation is a huge field where we can provide individual solutions - do not hesitate to get in touch - call us at <span style="color:#333">+49 211 555 01 92</span>.</p>
      <div class="btn" style="top:100px">View Details</div>
      <div class="photo" style="top:-6px;height:93px;background:linear-gradient(135deg,#e8f4fa 0%,#b8c4cc 30%,#3f8fc4 55%,#9aa6ae 85%,#dfeff7 100%)" role="img" aria-label="Silver touch panel industry computer"></div>
    </div>
    <div class="sep" style="top:333px"></div>

    <div class="product" style="top:352px">
      <h3>Embedded Systems for Industrial Automation</h3>
      <p style="top:22px">Velqora is your specialist partner for industrial automation. We at Velqora provide individual solutions for unitized measurement and offer the whole range of products, from interface converter over RS-485 and ModBus-Modules and to Embedded Systems and powerful Panel-PCs. Velqora is official partner of Norvel CCC. The Taiwanese specialist with the trademark VANTA is one of the leading manufacturers of reliable industrial hardware for unitized instrumentation control and automation.</p>
      <div class="btn" style="top:118px">View Details</div>
      <div class="photo" style="top:-7px;height:94px;background:linear-gradient(160deg,#dcedf7 0%,#7bb9dc 35%,#2f3538 55%,#8a9094 70%,#5aa3cf 100%)" role="img" aria-label="Fanless embedded box PC with front ports"></div>
    </div>
  </section>

  <footer class="abs footer">
    <h3 style="left:114px">Contact</h3>
    <div class="fcontact">
      <div style="display:flex;gap:6px">
        <svg width="12" height="11" viewBox="0 0 12 11"><path d="M6 0.5 L11.5 5.5 H10 V10.5 H7.3 V7.2 H4.7 V10.5 H2 V5.5 H0.5 Z" fill="#fff"/></svg>
        <div><b>Velqora Industrietechnik</b><br>Lindenweg 14, 40210 Düsseldorf</div>
      </div>
      <div style="display:flex;gap:6px;margin-top:12px;font-size:10.5px;font-weight:700;align-items:center">
        <svg width="11" height="11" viewBox="0 0 10 10"><path d="M2 0.5 L3.6 2.8 L2.8 4 Q4 6.2 6 7.2 L7.2 6.4 L9.5 8 L8.4 9.6 Q3.5 9 0.4 1.6 Z" fill="#fff"/></svg>
        +49 211 555 01 92
      </div>
      <div style="display:flex;gap:6px;margin-top:5px;align-items:center">
        <svg width="12" height="9" viewBox="0 0 12 9"><rect x="0.5" y="0.5" width="11" height="8" fill="none" stroke="#fff"/><path d="M0.5 0.5 L6 5 L11.5 0.5" stroke="#fff" fill="none"/></svg>
        <u>info@velqora.eu</u>
      </div>
    </div>
    <div class="fdiv" style="left:281px"></div>

    <h3 style="left:312px">Quick Links</h3>
    <ul class="quick">
      <li>» Home</li><li>» Solutions</li><li>» Products</li><li>» New &amp; Events</li><li>» Career</li><li>» Contact Us</li>
    </ul>
    <div class="fdiv" style="left:426px"></div>

    <h3 style="left:452px">Follow Us</h3>
    <div class="social"><span></span><span></span><span></span></div>
    <div class="fdiv" style="left:565px"></div>

    <h3 style="left:598px">Testimonials</h3>
    <div class="testi">
      <span style="font-size:16px;color:#7f95a3;font-family:Georgia,serif;line-height:0">“</span> Lorem ipsum dolor sit amet, consectetur adipisicing elit, sed do eiusmod tempor incididunt ut labore et dolore magna aliqua ...
      <div style="margin-top:8px"><b>Tomas</b> <span style="color:#b9dcec">&nbsp;- 05/01/11</span><span style="float:right;font-size:16px;color:#7f95a3;font-family:Georgia,serif">”</span></div>
    </div>
    <div class="readmore">READ MORE</div>
  </footer>

  <div class="abs bottom">
    <div class="abs" style="left:114px;top:7px">COPYRIGHT © <b>VELQORA INDUSTRIETECHNIK</b> 2013. ALL RIGHTS RESERVED.</div>
    <div class="abs" style="left:594px;top:7px">TERMS &amp; CONDITION &nbsp;&nbsp;&nbsp;&nbsp; | &nbsp;&nbsp;&nbsp;&nbsp; MASTHED</div>
  </div>

</div>
</body>
</html>
```